Pecan Ridge Paving. Chip Seal Done Right

I need my card to have all my basic information on it. Keep it simple. Include web site, phone number and email address. Include phrase Chip Seal Done Right or Pecan Ridge’s Top Paving Company. Keep card simple. Include color and logo. Put all contact info on card. Make card simple and not complicated.

Here is infuriation yo out in business card

Dale R. Whitmore
830.555.0173 cell phone
Dalewhitmore7@mailbarn.net
www.pecanridgepaving.net

Target Market(s)

Hill Country Texas USA

Industry/Entity Type

Road chip seal

Contact Information for Business Card

We chip seal roads for ranches and property owners

Font styles to use
Serif
Sans Serif
Decorative
Script

Colors
0054AA
0677BA
7BADD7
CADEEF
E8F1F8
EB3D1F
EC4F4E
F09395
F8D3D4
FCEDEE

Requirements
Must have
• Keep it simply
Nice to have
• Logo and all basic info

```html
<!DOCTYPE html>
<html lang="en">
<head>
<meta charset="utf-8">
<title>Pecan Ridge Paving – Business Card</title>
<link href="https://fonts.googleapis.com/css2?family=Lato:wght@400;700;900&display=swap" rel="stylesheet">
<style>
  :root {
    --backdrop: #a7a7a7;
    --navy: #1b2452;
    --red: #ad1f2d;
    --ink: #555a60;
    --paper: #ffffff;
  }
  * { margin: 0; padding: 0; box-sizing: border-box; }
  html, body { width: 1047px; height: 1200px; overflow: hidden; }
  body {
    background: var(--backdrop);
    font-family: "Lato", sans-serif;
    position: relative;
  }
  .card {
    position: absolute;
    left: 160px;
    width: 741px;
    height: 424px;
    overflow: hidden;
    box-shadow: 0 2px 5px rgba(0,0,0,0.25);
  }
  .card--front { top: 120px; background: var(--paper); }
  .card--back { top: 634px; background: var(--red); }

  .brand {
    position: absolute;
    left: 86px;
    top: 176px;
    display: flex;
    align-items: center;
    gap: 12px;
  }
  .brand__mark { width: 34px; height: 34px; background: var(--red); }
  .brand__name {
    font-weight: 900;
    font-size: 25px;
    line-height: 1.05;
    color: var(--navy);
    text-transform: uppercase;
  }
  .divider {
    position: absolute;
    left: 379px;
    top: 95px;
    width: 1px;
    height: 221px;
    background: var(--red);
  }
  .details { position: absolute; left: 416px; top: 90px; }
  .details__name {
    font-weight: 700;
    font-size: 30px;
    letter-spacing: 0.5px;
    color: var(--navy);
    line-height: 1.1;
  }
  .details__title { font-size: 19px; color: var(--red); margin-top: 2px; }
  .contact { list-style: none; margin-top: 17px; color: var(--ink); font-size: 17px; letter-spacing: 0.8px; }
  .contact li { display: flex; align-items: flex-start; line-height: 22px; }
  .contact li + li { margin-top: 4px; }
  .contact .gap { margin-top: 14px; }
  .contact svg { width: 14px; height: 14px; margin: 4px 14px 0 0; flex: none; fill: var(--red); }
  .band { position: absolute; left: 0; bottom: 0; width: 741px; height: 16px; }

  .back__name {
    position: absolute;
    left: 0; right: 0;
    top: 150px;
    text-align: center;
    font-weight: 900;
    font-size: 46px;
    color: var(--paper);
    text-transform: uppercase;
    letter-spacing: 1px;
  }
  .back__tagline {
    position: absolute;
    left: 0; right: 0;
    top: 371px;
    text-align: center;
    font-size: 21px;
    color: var(--paper);
    letter-spacing: 0.6px;
    text-transform: uppercase;
  }
  .back__tagline strong { font-weight: 900; }
</style>
</head>
<body>
  <section class="card card--front">
    <div class="brand">
      <span class="brand__mark"></span>
      <span class="brand__name">Pecan Ridge<br>Paving</span>
    </div>
    <div class="divider"></div>
    <div class="details">
      <h1 class="details__name">MICHAEL SMITH</h1>
      <p class="details__title">Founder &amp; CEO</p>
      <ul class="contact">
        <li>
          <svg viewBox="0 0 14 14"><path d="M7 0a4.5 4.5 0 0 0-4.5 4.5C2.5 8 7 14 7 14s4.5-6 4.5-9.5A4.5 4.5 0 0 0 7 0zm0 6.3a1.8 1.8 0 1 1 0-3.6 1.8 1.8 0 0 1 0 3.6z"/></svg>
          <span>1234 Main Street<br>City, State &amp; ZIP code<br>Country 89654</span>
        </li>
        <li class="gap">
          <svg viewBox="0 0 14 14"><path d="M3 1l2.2 2.8-1.2 1.6c.8 1.8 2.2 3.3 4 4.2l1.6-1.2L12.6 10 11 12.6C5.8 12 2 8 1.4 2.8z"/></svg>
          <span>(123) 456-7890</span>
        </li>
        <li>
          <svg viewBox="0 0 14 14"><path d="M1 3h12v1.2L7 8 1 4.2zM1 5.6l6 3.8 6-3.8V11H1z"/></svg>
          <span>michael@yourwebsite.com</span>
        </li>
        <li>
          <svg viewBox="0 0 14 14"><circle cx="7" cy="7" r="6.3"/><path d="M4 4.5c1.5-.5 2.5.5 2 1.5s-2 .5-2 2 1.5 2 1.5 3.5M9 3c-.5 1 .5 2 1.5 2M10.5 8.5c-1 0-1.5 1-1 2" stroke="#fff" stroke-width="1" fill="none"/></svg>
          <span>www.yourwebsite.com</span>
        </li>
      </ul>
    </div>
    <svg class="band" viewBox="0 0 741 16" preserveAspectRatio="none" aria-hidden="true">
      <rect x="0" y="2" width="741" height="14" fill="var(--navy)"/>
      <path d="M578 2 Q590 14 614 16 L741 16 L741 2 Z" fill="var(--paper)"/>
      <path d="M588 2 Q600 12 622 16 L741 16 L741 2 Z" fill="var(--red)"/>
    </svg>
  </section>

  <section class="card card--back">
    <p class="back__name">Pecan Ridge Paving</p>
    <p class="back__tagline">Pecan Ridge’s <strong>Top Paving Company</strong></p>
  </section>
</body>
</html>
```